Harbor Perks business cards
Harbor Perks stationary
Harbor Perks business cards - Employment
Creative Brief
Bright & Fun-filled
Tom Varnick
Benefit Consultant
927 N. 610 E. Brindlefield, Utah 84592
tom@harborperksmail.com
www.harborperksmail.com
I am looking for a design that is professional, but communicates that we give employees a reason to appreciate and enjoy their job. We help employers attract and keep great employees by providing rewards and incentives. Please don't put address on the business card.

```html
<!DOCTYPE html>
<html lang="en">
<head>
<meta charset="utf-8">
<title>Harbor Perks business cards</title>
<link href="https://fonts.googleapis.com/css2?family=Arimo:wght@700&family=Tinos:wght@400;700&display=swap" rel="stylesheet">
<style>
  :root {
    --page: #ffffff;
    --blue-light: #2a93c4;
    --blue-mid: #1572a3;
    --blue-deep: #0b4c72;
    --swoosh: #3a3f44;
    --swoosh-soft: #7c8790;
    --ink: #4a4f54;
    --white: #ffffff;
  }
  * { margin: 0; padding: 0; box-sizing: border-box; }
  html, body {
    width: 1200px; height: 324px; overflow: hidden;
    background: var(--page);
  }
  .sheet { position: relative; width: 1200px; height: 324px; }
  .card {
    position: absolute; top: 5px;
    width: 571px; height: 314px; overflow: hidden;
    background: linear-gradient(160deg, var(--blue-light) 0%, var(--blue-mid) 45%, var(--blue-deep) 100%);
  }
  .card--front { left: 12px; }
  .card--back { left: 617px; }
  .card__art { position: absolute; inset: 0; }
  .brand {
    position: absolute; left: 356px; top: 30px;
    display: flex; align-items: center; gap: 10px;
    white-space: nowrap;
  }
  .brand__dot {
    flex: none;
    width: 30px; height: 30px; border-radius: 50%;
    background: var(--blue-mid);
  }
  .brand__name {
    font-family: "Arimo", Arial, sans-serif;
    font-weight: 700; font-size: 26px; line-height: 1; color: var(--ink);
    letter-spacing: -0.3px;
  }
  .person {
    position: absolute; left: 28px; top: 226px;
    font-family: "Tinos", "Times New Roman", serif;
    color: var(--white);
  }
  .person__name { font-weight: 700; font-size: 19px; line-height: 26px; }
  .person__role { font-size: 18px; line-height: 24px; }
  .contact {
    position: absolute; right: 24px; top: 228px;
    font-family: "Tinos", "Times New Roman", serif;
    color: var(--white); font-size: 15px; line-height: 24px;
    text-align: right; white-space: nowrap;
  }
  .contact b { font-weight: 700; }
  .divider {
    position: absolute; left: 240px; top: 226px;
    width: 1px; height: 80px; background: rgba(255,255,255,0.55);
  }
</style>
</head>
<body>
<div class="sheet">

  <section class="card card--front">
    <svg class="card__art" viewBox="0 0 571 314" width="571" height="314" aria-hidden="true">
      <ellipse cx="360" cy="-30" rx="410" ry="175" fill="var(--swoosh-soft)"/>
      <ellipse cx="340" cy="-40" rx="398" ry="168" fill="var(--swoosh)"/>
      <ellipse cx="300" cy="-55" rx="390" ry="170" fill="var(--white)"/>
    </svg>
    <div class="brand"><span class="brand__dot"></span><span class="brand__name">Harbor Perks</span></div>
    <div class="person">
      <p class="person__name">Tom Varnick</p>
      <p class="person__role">Benefit Consultant</p>
    </div>
    <div class="divider"></div>
    <div class="contact">
      <p><b>Cell :</b> 801-555-0147</p>
      <p><b>Email :</b> tom@harborperksmail.com</p>
      <p><b>Web :</b> www.harborperksmail.com</p>
    </div>
  </section>

  <section class="card card--back">
    <svg class="card__art" viewBox="0 0 571 314" width="571" height="314" aria-hidden="true">
      <path d="M180 314 C260 200 420 150 571 160 L571 314 Z" fill="rgba(255,255,255,0.06)"/>
      <path d="M330 314 C380 240 470 210 571 215 L571 314 Z" fill="rgba(255,255,255,0.05)"/>
      <ellipse cx="360" cy="-30" rx="410" ry="175" fill="var(--swoosh-soft)"/>
      <ellipse cx="340" cy="-40" rx="398" ry="168" fill="var(--swoosh)"/>
      <ellipse cx="300" cy="-55" rx="390" ry="170" fill="var(--white)"/>
    </svg>
    <div class="brand"><span class="brand__dot"></span><span class="brand__name">Harbor Perks</span></div>
    <div class="person">
      <p class="person__name">Tom Varnick</p>
      <p class="person__role">Benefit Consultant</p>
    </div>
    <div class="contact">
      <p><b>Cell :</b> 801-555-0147</p>
      <p><b>Email :</b> tom@harborperksmail.com</p>
      <p><b>Web :</b> www.harborperksmail.com</p>
    </div>
  </section>

</div>
</body>
</html>
```